依頼詳細
会社の名刺デザインを新しくしたいと思っています。
今回ご提案頂きたいのは、「真面目でシンプルなデザイン」か「遊び心あるデザイン」どちらかの提案を希望しております。基本的にはロゴのイメージに合うようなデザインでお願いします。
名刺の背景は白地でお願い致します。
色、デザイン、表現はお任せ致しますが、独創性が感じられる名刺にしたいという想いがありますので、検討して頂けたら幸いです。
記載項目
【記載内容】
ロゴ(添付ファイル)
会社名(日本語):株式会社Talbrio
(英語) :Talbrio Inc.
役職(日本語、英語)
名前(日本語、英語)
Email
携帯電話
郵便番号
住所
TEL
FAX
URL

※ 表面を日本語、裏面を英語にする等、表現はお任せ致します。(英語無しでも構いません)
希望イメージ
シンプル 複雑
単色 カラフル
暗い 明るい
日常 高級
遊び心 厳粛
未来的 伝統的
女性的 男性的
希望する色
お任せします
納品ファイル
• 高解像度JPG (.jpg)
• イラストレーター形式 (.ai)
• フォトショップ形式 (.psd)
補足説明
ロゴファイルは2パターン3色の6種類を用意致しますので、お好きなロゴをお使いご提案お願い致します。
またロゴの文字色を変更しても構いません。
宜しくお願い致します。
たくさんのご提案ありがとうございます。
現状の提案を見ると直線を用いたデザインが多いので、曲線を用いたデザインのご提案を検討して頂ければと思います。
宜しくお願いします。
■ 選んだ理由

非常に多くのご応募を頂き他の候補と最後の最後まで悩んだのですが、2パターンのデザインがあったこと、シンプルでありロゴのイメージあっていることが決め手となりました。
とても満足のいく名刺になりました。
どうもありがとうございます。

■ 提案者全員のお礼・コメント

沢山のご応募頂き、皆様にはとても感謝しております。
そのため選定まで時間がかかってしまったことをお詫び申し上げます。
今後とも、どうか宜しくお願い致します。

```html
<!DOCTYPE html>
<html lang="ja">
<head>
<meta charset="utf-8">
<title>Talbrio Inc. Business Card</title>
<link rel="stylesheet" href="https://fonts.googleapis.com/css2?family=Arimo:wght@400;700&family=Montserrat:wght@600&display=swap">
<style>
  :root {
    --teal: #1f9aa6;
    --teal-dark: #137985;
    --ink: #1c1c1c;
    --brown: #2a1b17;
    --paper: #ffffff;
  }
  html, body {
    margin: 0;
    padding: 0;
    width: 727px;
    height: 1200px;
    overflow: hidden;
    background: var(--paper);
  }
  .card {
    position: relative;
    width: 727px;
    height: 1200px;
    background: var(--paper);
    font-family: "Arimo", Arial, sans-serif;
    color: var(--ink);
    overflow: hidden;
  }
  .wave-top, .wave-bottom {
    position: absolute;
    left: 0;
    display: block;
  }
  .wave-top { top: 0; }
  .wave-bottom { bottom: 0; }
  .brand {
    position: absolute;
    top: 130px;
    left: 0;
    width: 727px;
    text-align: center;
    font-family: "Montserrat", Arial, sans-serif;
    font-weight: 600;
    font-size: 96px;
    letter-spacing: 2px;
    color: var(--brown);
    line-height: 1;
  }
  .person {
    position: absolute;
    left: 165px;
    top: 492px;
  }
  .person .title {
    font-size: 29px;
    margin: 0 0 14px;
  }
  .person .name {
    font-size: 42px;
    letter-spacing: 1px;
    margin: 0;
    font-weight: 400;
  }
  .company {
    position: absolute;
    left: 108px;
    top: 660px;
  }
  .company .company-name {
    font-size: 32px;
    font-weight: 700;
    margin: 0 0 14px;
  }
  .contact {
    list-style: none;
    margin: 0;
    padding: 0;
    font-size: 26px;
    line-height: 39.5px;
  }
  .contact li {
    display: flex;
    align-items: center;
    white-space: nowrap;
  }
  .contact .indent { padding-left: 4px; }
  .tag {
    display: inline-flex;
    align-items: center;
    justify-content: center;
    min-width: 30px;
    height: 24px;
    padding: 0 2px;
    margin-right: 4px;
    background: var(--teal);
    color: var(--paper);
    font-size: 15px;
    font-weight: 700;
    border-radius: 2px;
    box-sizing: border-box;
  }
  .tag.small { font-size: 11px; }
  .tag svg { display: block; }
</style>
</head>
<body>
<div class="card">
  <svg class="wave-top" width="727" height="130" viewBox="0 0 727 130" aria-hidden="true">
    <path d="M0 0 H727 V42 C600 78 470 30 330 38 C200 46 90 95 0 88 Z" fill="var(--teal)"/>
    <path d="M0 0 H727 V18 C600 40 470 10 330 18 C200 26 90 60 0 55 Z" fill="var(--teal-dark)" opacity="0.35"/>
  </svg>

  <div class="brand">Talbrio</div>

  <section class="person">
    <p class="title">Yakushoku</p>
    <h1 class="name">HARUTO SAKAI</h1>
  </section>

  <section class="company">
    <p class="company-name">Talbrio Inc.</p>
    <ul class="contact">
      <li><span class="tag">〒</span>1-1-1○○○○○○○○○○○○○○ ○○</li>
      <li class="indent">000-0000 JAPAN</li>
      <li><span class="tag">TEL</span>+81-03-0000-0000</li>
      <li><span class="tag">FAX</span>+81-03-0000-0000</li>
      <li><span class="tag small">Mobile</span>+81-80-0000-0000</li>
      <li><span class="tag"><svg width="22" height="16" viewBox="0 0 22 16"><rect x="1" y="1" width="20" height="14" fill="none" stroke="#fff" stroke-width="2"/><path d="M1 1 L11 9 L21 1" fill="none" stroke="#fff" stroke-width="2"/></svg></span>info@talbrio.co.jp</li>
      <li><span class="tag">URL</span>http://www.talbrio.jp/</li>
    </ul>
  </section>

  <svg class="wave-bottom" width="727" height="240" viewBox="0 0 727 240" aria-hidden="true">
    <path d="M0 10 C180 40 420 55 560 40 C640 32 700 20 727 12" fill="none" stroke="var(--teal)" stroke-width="4"/>
    <path d="M0 22 C180 52 420 68 560 52 C640 44 700 32 727 24 V240 H0 Z" fill="var(--brown)"/>
  </svg>
</div>
</body>
</html>
```